Roofing & Siding door hanger flyer

-Looking to make door hanger flyer for Pellmont Roofing & Siding
-4.5" wide x 11" tall
-2 sided full colour
-We have started a new website (the content is changing) I have attached photos.
-About us:
-25 year labour warranty's available
-32 years in Calgary
-QCR A+ Member
-NWTG (Prairie Joint Shingle Guild) (logo attached)
-KOV Summit Select (logo attached)
-Owen Brisket (logo attached)
-Slogan "Raised On Care, Proven Through Seasons" 32 years in Calgary
-Sale
-Page 1 & 2 design ideas
We are in your area, contact us today for your Exclusive limited time offer! *discounts apply exclusively to new agreements only
Updates
-Please keep simple, clean & bright
-I really like the bright blue from our new logo (new logo uploaded)
-We specialize in Roofing -Siding-Gutters & full Exterior Renos (like the competitor example uploaded)
-This is the NEW website we are currently working on (not finished) https://mockview.example-draftpad.net/view/1a2b3c4d-5e6f-4a7b-8c9d-0e1f2a3b4c5d-7k2m/?fullscreen
-This is our OLD website https://pellmontshingleworks.com
-For the sale "We are in your area, contact us today for your Exclusive limited time offer" *discounts apply exclusively to new agreements only
-Free Estimates
-our phone# is 403-555-0148
-our website is pellmontshingleworks.com
-keep simple, clean, bright use the "new logo" uploaded. Check out the competitor example uploaded file
-We are in your area, Contact us today for your Exclusive limited time offer! *discounts apply to new agreements only
-FREE ESTIMATES
-Specialized in Roofing /Siding /Gutters Full Exterior Reno's
-We are currently working on a NEW website https://mockview.example-draftpad.net/view/1a2b3c4d-5e6f-4a7b-8c9d-0e1f2a3b4c5d-7k2m/?fullscreen
-Our OLD website https://pellmontshingleworks.com/
-Post old site address on flyer pellmontshingleworks.com
-Phone # 403-555-0148
Target Market(s)
40-55
Industry/Entity Type
Roofing Siding & full Exterior Reno's
Look and feel

```html
<!DOCTYPE html>
<html lang="en">
<head>
<meta charset="utf-8">
<title>Pellmont Roofing &amp; Siding – Door Hanger</title>
<link href="https://fonts.googleapis.com/css2?family=Rubik:wght@400;500;700&display=swap" rel="stylesheet">
<style>
:root{
  --stage:#8a8a8c;
  --paper:#ffffff;
  --ink:#1c1c1c;
  --ink-soft:#4a4a4a;
  --brand:#1f6fc1;
  --brand-deep:#1d63b4;
  --band:#2f7dc3;
  --strip:#f1f2f3;
  --white:#ffffff;
}
*{box-sizing:border-box;margin:0;padding:0}
html,body{width:1200px;height:1200px;overflow:hidden}
body{background:var(--stage);font-family:"Rubik",sans-serif;color:var(--ink);position:relative}

.hanger{position:absolute;top:77px;width:437px;height:1068px;overflow:hidden;
  background:
    repeating-linear-gradient(170deg,rgba(0,0,0,0) 0 9px,rgba(0,0,0,.025) 9px 11px),
    linear-gradient(180deg,#fff 0%,#f2f3f4 22%,#f7f7f8 45%,#fff 70%,#f4f5f6 100%);}
.hanger--front{left:128px}
.hanger--back{left:630px;height:1070px}

.hang-hole{position:absolute;left:146px;top:111px;width:145px;height:145px;border:1px solid #666;border-radius:50%}

.headline{position:absolute;left:0;right:0;text-align:center}
.headline__lead{font-size:24px;font-weight:400;color:var(--ink)}
.headline__main{font-size:46px;font-weight:500;color:var(--brand);letter-spacing:-.5px;line-height:1.05}

.brand{position:absolute;left:0;right:0;text-align:center;color:var(--ink)}
.brand__est{font-size:13px;letter-spacing:2px;color:var(--ink-soft);margin-bottom:6px}
.brand__name{font-size:44px;font-weight:500;letter-spacing:4px;line-height:1}
.brand__sub{font-size:20px;font-weight:400;color:#3a3a3a;letter-spacing:5px;margin-top:10px}

.service{position:absolute;left:20px;width:397px;border-radius:14px;overflow:hidden;background:var(--brand-deep)}
.service__photo{position:absolute;inset:0}
.service__tab{position:absolute;top:0;background:var(--paper);color:var(--brand-deep);font-weight:700;font-size:22px;display:flex;align-items:center;justify-content:center;letter-spacing:.3px}
.service__list{position:absolute;list-style:none;color:var(--white);font-size:13.5px;line-height:16.2px}
.service__list li{position:relative;padding-left:16px}
.service__list li::before{content:"";position:absolute;left:2px;top:3px;width:4px;height:8px;border:solid var(--white);border-width:0 1.5px 1.5px 0;transform:rotate(45deg)}

.service--roofing{top:444px;height:169px}
.service--roofing .service__photo{background:linear-gradient(180deg,#6aa7d8 0%,#a9c9e4 35%,#5d5f63 55%,#e8e4d6 78%,#3f5e35 100%);clip-path:polygon(120px 0,100% 0,100% 100%,168px 100%)}
.service--roofing .service__tab{right:0;width:131px;height:32px;border-bottom-left-radius:12px}
.service--roofing .service__list{left:20px;top:30px}

.service--siding{top:620px;height:169px;left:22px}
.service--siding .service__photo{background:linear-gradient(180deg,#b7cde3 0%,#dfe4ea 40%,#c9ccd1 70%,#6e6a66 100%);clip-path:polygon(0 0,267px 0,218px 100%,0 100%)}
.service--siding .service__tab{left:0;width:118px;height:29px;border-bottom-right-radius:12px}
.service--siding .service__list{left:272px;top:40px}

.service--exterior{top:796px;height:176px}
.service--exterior .service__photo{background:linear-gradient(180deg,#5d9ad1 0%,#a9c7e2 30%,#8a6f5c 52%,#6f8c4a 78%,#7cb342 100%);clip-path:polygon(130px 0,100% 0,100% 100%,187px 100%)}
.service--exterior .service__tab{right:0;width:203px;height:33px;border-bottom-left-radius:12px}
.service--exterior .service__list{left:20px;top:18px}

.contact{position:absolute;left:0;right:0;text-align:center}
.contact__phone{display:flex;align-items:center;justify-content:center;gap:4px;font-size:31px;font-weight:700;color:var(--brand-deep);line-height:1}
.contact__phone svg{width:27px;height:27px}
.contact__web{font-size:23px;color:#333;margin-top:6px;letter-spacing:.2px}

.showcase{position:absolute;left:0;top:453px;width:100%;height:243px;
  background:linear-gradient(180deg,#8fb2e0 0%,#d9a9c4 12%,#3a3d44 40%,#2a2c31 65%,#4f5a2d 88%,#3f4a22 100%)}
.showcase__title{position:absolute;top:12px;left:0;right:0;text-align:center;color:var(--white);font-size:22px;font-weight:400}
.warranty{position:absolute;bottom:12px;display:flex;align-items:flex-end;gap:6px;color:var(--white)}
.warranty__big{font-size:29px;line-height:1}
.warranty__small{font-size:11px;line-height:13px}
.warranty--labour{left:40px}
.warranty--local{left:265px}

.badges{position:absolute;left:0;top:696px;width:100%;height:77px;background:var(--strip);display:flex;align-items:center;justify-content:space-around;padding:0 20px}
.badge{background:#c9ced6}
.badge--diamond{width:36px;height:36px;transform:rotate(45deg);background:#2a3b7a}
.badge--round{width:28px;height:28px;border-radius:50%;background:#3c9a4a}
.badge--wide{width:150px;height:30px;border-radius:4px;background:#d3d9e2}
.badge--box{width:63px;height:44px;border-radius:5px;background:var(--white);border:1px solid #555}

.offer{position:absolute;left:0;top:773px;width:100%;height:183px;background:var(--band);color:var(--white);text-align:center;padding-top:18px}
.offer__lead{font-size:24px}
.offer__main{font-size:45px;font-weight:500;line-height:1.05;letter-spacing:-.3px}
.offer__cta{font-size:30px;line-height:1.15}
.offer__note{font-size:21px;margin-top:2px}
</style>
</head>
<body>

<section class="hanger hanger--front">
  <div class="headline" style="top:22px">
    <div class="headline__lead">We’re in Your</div>
    <div class="headline__main">Neighbourhood!</div>
  </div>
  <div class="hang-hole"></div>

  <div class="brand" style="top:318px">
    <div class="brand__est">Est. 1991</div>
    <div class="brand__name">PELLMONT</div>
    <div class="brand__sub">ROOFING &amp; SIDING</div>
  </div>

  <article class="service service--roofing">
    <div class="service__photo" role="img" aria-label="Photo of a house with a new shingle roof and dormers"></div>
    <div class="service__tab">ROOFING</div>
    <ul class="service__list"><li>Asphalt</li><li>Rubber</li><li>Metal</li></ul>
  </article>

  <article class="service service--siding">
    <div class="service__photo" role="img" aria-label="Photo of a white two-storey home with board and batten siding"></div>
    <div class="service__tab">SIDING</div>
    <ul class="service__list"><li>Brisket fibre<br>cement</li><li>Vinyl</li><li>Metal (Steel,<br>Aluminum)</li><li>Longboard</li></ul>
  </article>

  <article class="service service--exterior">
    <div class="service__photo" role="img" aria-label="Photo of a brick and siding home with landscaped front garden"></div>
    <div class="service__tab">FULL EXTERIOR</div>
    <ul class="service__list"><li>Edvestrough/</li><li>Soffit/Fdscid</li><li>Stone</li><li>Skylight</li><li>Windows &amp; Doors</li><li>Stucco</li><li>Insulation</li><li>painting</li><li>Shake Repairs</li></ul>
  </article>

  <div class="contact" style="top:984px">
    <div class="contact__phone">
      <svg viewBox="0 0 24 24" fill="none" stroke="currentColor" stroke-width="1.6"><circle cx="12" cy="12" r="10.5"/><path d="M8.2 6.5l1.8-.3 1 2.6-1.2 1c.6 1.5 1.8 2.8 3.3 3.4l1-1.2 2.6 1-.3 1.8c-.2.7-.9 1.1-1.6 1-3.9-.6-6.6-3.4-7.2-7.2-.1-.7.3-1.3.6-2.1z"/></svg>
      <span>403-555-0148</span>
    </div>
    <div class="contact__web">www.pellmontshingleworks.com</div>
  </div>
</section>

<section class="hanger hanger--back">
  <div class="hang-hole"></div>

  <div class="brand" style="top:324px">
    <div class="brand__est">Est. 1991</div>
    <div class="brand__name">PELLMONT</div>
    <div class="brand__sub">ROOFING &amp; SIDING</div>
  </div>

  <div class="showcase" role="img" aria-label="Photo of a modern dark-sided home with stone entry and warm lights at dusk">
    <div class="showcase__title">Raised On Care, Proven Through Seasons</div>
    <div class="warranty warranty--labour"><span class="warranty__big">25 year</span><span class="warranty__small">labour<br>warranty’s available</span></div>
    <div class="warranty warranty--local"><span class="warranty__big">32 year</span><span class="warranty__small">in<br>Calgary</span></div>
  </div>

  <div class="badges">
    <span class="badge badge--diamond"></span>
    <span class="badge badge--round"></span>
    <span class="badge badge--wide"></span>
    <span class="badge badge--box"></span>
  </div>

  <div class="offer">
    <div class="offer__lead">We’re in Your</div>
    <div class="offer__main">Neighbourhood!</div>
    <div class="offer__cta">Contact us today</div>
    <div class="offer__note">for your Exclusive limited time offer!</div>
  </div>

  <div class="contact" style="top:980px">
    <div class="contact__phone">
      <svg viewBox="0 0 24 24" fill="none" stroke="currentColor" stroke-width="1.6"><circle cx="12" cy="12" r="10.5"/><path d="M8.2 6.5l1.8-.3 1 2.6-1.2 1c.6 1.5 1.8 2.8 3.3 3.4l1-1.2 2.6 1-.3 1.8c-.2.7-.9 1.1-1.6 1-3.9-.6-6.6-3.4-7.2-7.2-.1-.7.3-1.3.6-2.1z"/></svg>
      <span>403-555-0148</span>
    </div>
    <div class="contact__web">www.pellmontshingleworks.com</div>
  </div>
</section>

</body>
</html>
```